Dental specialist needs a sharp looking letterhead

I am looking for a letterhead to be used to send letters and communication between myself (a dental specialist) and other dentists.
My office is a state of the art dental specialty office.
I need to letterhead to also state:
Derek L. Halvorsen DDS
2847 Birchmont Avenue, Suite K
West Larkdale, NY 14390
(716)555-0193
fax: (716)555-0157
halvorsenpulp.com (**this email address may change)

i included my logo designs.
thank you

Target Market(s)

dentists

Industry/Entity Type

Communication

Requirements
Must have
• the included logo, whether the vertical or horizontal versions

```html
<!DOCTYPE html>
<html lang="en">
<head>
<meta charset="utf-8">
<title>Northgate Endodontics P.C. – Letterhead</title>
<link rel="stylesheet" href="https://fonts.googleapis.com/css2?family=Arimo:wght@400&display=swap">
<style>
  :root {
    --paper: #ffffff;
    --ink: #1a1a1a;
    --brand-blue: #3fa6dc;
    --wash-blue: #d9ebf7;
    --wash-green: #e5f1da;
  }
  html, body {
    margin: 0;
    padding: 0;
    width: 927px;
    height: 1200px;
    overflow: hidden;
    background: var(--paper);
  }
  .letterhead {
    position: relative;
    width: 927px;
    height: 1200px;
    background: var(--paper);
    font-family: "Arimo", Arial, sans-serif;
    color: var(--ink);
    overflow: hidden;
  }
  .brand {
    position: absolute;
    left: 64px;
    top: 70px;
    display: flex;
    align-items: center;
    gap: 16px;
  }
  .brand-dot {
    width: 44px;
    height: 44px;
    border-radius: 50%;
    background: var(--brand-blue);
    flex: none;
  }
  .brand-name {
    font-size: 27px;
    line-height: 1.25;
    color: var(--ink);
    letter-spacing: 0.5px;
  }
  .contact {
    position: absolute;
    left: 694px;
    top: 50px;
    margin: 0;
    font-style: normal;
    font-size: 11.5px;
    line-height: 15px;
  }
  .contact .doctor {
    display: block;
    font-size: 14.5px;
    line-height: 20px;
  }
  .contact .gap { display: block; height: 6px; }
  .corner-wash {
    position: absolute;
    right: 0;
    bottom: 0;
    width: 520px;
    height: 540px;
  }
</style>
</head>
<body>
  <main class="letterhead">
    <header class="brand">
      <span class="brand-dot"></span>
      <span class="brand-name">Northgate Endodontics P.C.</span>
    </header>

    <address class="contact">
      <span class="doctor">Derek L. Halvorsen DDS</span>
      2847 Birchmont Avenue, Suite K<br>
      West Larkdale, NY 14390<br>
      <span class="gap"></span>
      tel: (716)555-0193<br>
      <span class="gap"></span>
      fax: (716)555-0157<br>
      halvorsenpulp.com
    </address>

    <svg class="corner-wash" viewBox="0 0 520 540" aria-hidden="true">
      <circle cx="430" cy="430" r="300" fill="var(--wash-blue)" opacity="0.8"/>
    </svg>
  </main>
</body>
</html>
```